New florist business website design

Number 1 want is an easy to navigate & check out website
Needs to be beautiful and eye catching as well.
This is an online only business (no shop front)
Rustic and blush pinks, neutrals, woods, leaves
Customers need to be able to go onto my website, select something they want to buy but have the option to use a drop down box to change colours of the flowers, or add notes to make changes to the arrangement

Industry/Entity Type

Florist

Coding

Coded - Design and coding required

Number of Pages Required

5+ page

Colors
f9d9e8
fff2ec
fffefc

Requirements
Must have
• Drop down menu to take you to other pages for Arrangements, bouquets, everlasting arrangements, gifts, contact
Be able to purchase and “add to basket”
Checkout page
Nice to have
• Be able to add my own photos once I’ve taken new ones
Should not have
• Tacky images or clip art

```html
<!DOCTYPE html>
<html lang="en">
<head>
<meta charset="utf-8">
<title>Bloom &amp; Bough — Florist</title>
<link href="https://fonts.googleapis.com/css2?family=Josefin+Sans:wght@300;400;600&family=Lato:wght@400;700&family=Mrs+Saint+Delafield&display=swap" rel="stylesheet">
<style>
:root{
  --blush:#f9d9e8;
  --cream:#fff2ec;
  --paper:#fffefc;
  --hero:#fde8e3;
  --ink:#1c1c1c;
  --muted:#555;
  --line:#cfc6c2;
  --rose:#e8a9c4;
  --leaf:#6f8a4e;
}
*{box-sizing:border-box;margin:0;padding:0}
html,body{width:1200px;height:4758px;overflow:hidden}
body{position:relative;background:var(--paper);color:var(--ink);font-family:"Lato",sans-serif}
.abs{position:absolute}
.heading{font-family:"Josefin Sans",sans-serif;font-weight:400}
.script{font-family:"Mrs Saint Delafield",cursive;font-weight:400}
.center{text-align:center}
.btn{position:absolute;border:2px solid var(--ink);border-radius:40px;display:flex;align-items:center;justify-content:center;gap:8px;font-family:"Lato",sans-serif;font-weight:700;font-size:13px;letter-spacing:.5px;background:transparent}
.ornament{position:absolute;width:96px;height:22px;left:552px;border-radius:50%;background:radial-gradient(ellipse,#d9d2cf 0%,rgba(217,210,207,0) 70%)}
/* nav */
.nav-link{position:absolute;top:75px;font-size:15px;font-family:"Lato",sans-serif}
.logo{position:absolute;font-family:"Josefin Sans",sans-serif;font-weight:300;color:var(--ink);white-space:nowrap}
/* hero */
.hero{left:0;top:0;width:1200px;height:807px;background:var(--hero)}
.hero-photo{left:500px;top:150px;width:700px;height:657px;background:radial-gradient(circle at 65% 30%,#f2c9b4 0%,#f6dacd 25%,rgba(253,232,227,0) 55%),radial-gradient(circle at 35% 60%,#f07a93 0%,#f2c53a 20%,#5c8a3e 42%,rgba(253,232,227,0) 65%)}
.dot{position:absolute;width:7px;height:7px;border-radius:50%;background:var(--ink)}
.dot.open{background:transparent;border:1.5px solid var(--ink);width:9px;height:9px}
/* features */
.feature-icon{position:absolute;width:80px;height:80px;border-radius:50%;display:flex;align-items:center;justify-content:center}
.feature-title{position:absolute;width:300px;font-size:28px}
.feature-cap{position:absolute;width:320px;font-size:12px;letter-spacing:.2px}
.divider{position:absolute;width:1px;height:111px;top:945px;background:var(--line)}
/* products */
.product-card{left:310px;top:1325px;width:272px;height:410px;border-radius:28px;background:var(--cream)}
.product-img{position:absolute;width:150px;height:200px;top:1357px;border-radius:40px}
.product-name{position:absolute;width:220px;top:1577px;font-size:17px;text-align:center}
.product-price{position:absolute;width:220px;top:1601px;font-size:38px;font-family:"Lato",sans-serif;font-weight:700;text-align:center}
/* welcome */
.welcome{left:0;top:1815px;width:1200px;height:570px;background:var(--blush)}
/* blog */
.blog-img{position:absolute;top:2643px;width:321px;height:227px;border-radius:34px}
.blog-date{position:absolute;top:2837px;width:66px;height:66px;border-radius:50%;background:var(--cream);display:flex;flex-direction:column;align-items:center;justify-content:center;font-size:12px;font-weight:700;line-height:1.1}
.blog-title{position:absolute;top:2918px;width:321px;font-size:26px;text-align:center}
.blog-text{position:absolute;top:2966px;width:321px;font-size:11px;line-height:1.6;color:var(--muted);text-align:center}
.read-more{position:absolute;top:3038px;width:321px;font-size:12px;color:#888;text-align:center;text-decoration:underline}
/* testimonial */
.quote-mark{font-family:"Josefin Sans",sans-serif;font-size:30px;font-weight:600;line-height:0;vertical-align:-10px}
/* photo feed */
.insta-tile{position:absolute;top:3812px;width:210px;height:209px}
/* footer */
.footer{left:0;top:4283px;width:1200px;height:428px;background:var(--cream)}
.newsletter{left:74px;top:4205px;width:1052px;height:148px;border-radius:40px;background:var(--blush)}
.foot-h{position:absolute;top:4416px;font-size:26px}
.foot-list{position:absolute;list-style:none;font-size:12px;font-weight:700;line-height:16px}
.contact-row{position:absolute;display:flex;gap:12px;font-size:12px;line-height:14px}
.social-row{position:absolute;display:flex;align-items:center;gap:10px;font-size:12px}
.social-row i{display:block;width:12px;height:12px;border-radius:50%;background:var(--ink)}
.bottom-bar{left:0;top:4711px;width:1200px;height:47px;background:var(--blush)}
.pay-chip{position:absolute;top:4722px;width:42px;height:24px;border-radius:4px;background:#fff;font-size:9px;font-weight:700;display:flex;align-items:center;justify-content:center;color:#333}
</style>
</head>
<body>

<!-- Hero -->
<section class="abs hero"></section>
<div class="abs hero-photo" role="img" aria-label="Woman smiling with eyes closed, holding a large bouquet of pink, yellow and white lilies"></div>

<nav>
  <a class="nav-link" style="left:72px">Home</a>
  <a class="nav-link" style="left:157px">Shop</a>
  <a class="nav-link" style="left:233px">About</a>
  <a class="nav-link" style="left:318px">Blogs</a>
  <a class="nav-link" style="left:398px">Contact</a>
</nav>
<div class="logo" style="left:520px;top:70px;font-size:28px">Bloom &amp; Bough</div>
<svg class="abs" style="left:956px;top:64px" width="26" height="26" viewBox="0 0 26 26" fill="none" stroke="#1c1c1c" stroke-width="1.8"><circle cx="15" cy="10" r="6"/><line x1="11" y1="14" x2="3" y2="22"/></svg>
<svg class="abs" style="left:1020px;top:62px" width="32" height="30" viewBox="0 0 32 30" fill="none" stroke="#1c1c1c" stroke-width="1.8"><path d="M4 9h20l-2 17H6z"/><path d="M9 9V6a5 5 0 0 1 10 0v3"/><circle cx="25" cy="22" r="6" fill="#1c1c1c"/><text x="25" y="25.5" font-size="9" fill="#fff" stroke="none" text-anchor="middle" font-family="Lato">2</text></svg>
<svg class="abs" style="left:1090px;top:64px" width="32" height="24" viewBox="0 0 32 24" stroke="#1c1c1c" stroke-width="2"><line x1="2" y1="3" x2="30" y2="3"/><line x1="10" y1="10" x2="30" y2="10"/><line x1="2" y1="17" x2="30" y2="17"/><line x1="14" y1="23" x2="30" y2="23"/></svg>

<div class="abs heading" style="left:92px;top:318px;font-size:29px;line-height:37px">GORGEOUS<br>FLOWERS FOR YOUR</div>
<div class="abs script" style="left:84px;top:402px;font-size:74px;line-height:1">Special Events</div>
<a class="btn" style="left:135px;top:484px;width:170px;height:46px">SHOP NOW</a>
<span class="dot" style="left:74px;top:748px"></span>
<span class="dot open" style="left:87px;top:747px"></span>
<span class="dot" style="left:102px;top:748px"></span>
<span class="dot" style="left:116px;top:748px"></span>

<!-- Features -->
<div class="feature-icon" style="left:210px;top:902px;background:var(--blush)">
  <svg width="36" height="36" viewBox="0 0 36 36" fill="none" stroke="#1c1c1c" stroke-width="1.5"><path d="M6 24L30 6l-6 26-7-9z"/><line x1="17" y1="23" x2="30" y2="6"/></svg>
</div>
<div class="feature-icon" style="left:570px;top:902px;background:var(--cream)">
  <svg width="34" height="34" viewBox="0 0 34 34" fill="none" stroke="#1c1c1c" stroke-width="1.5"><path d="M8 4l6 6-3 4c2 4 5 7 9 9l4-3 6 6-4 5C14 30 4 20 4 8z"/></svg>
</div>
<div class="feature-icon" style="left:940px;top:902px;background:var(--paper);box-shadow:0 2px 10px rgba(0,0,0,.08)">
  <span style="font-size:32px;font-family:'Josefin Sans',sans-serif">$</span>
</div>
<div class="divider" style="left:421px"></div>
<div class="divider" style="left:796px"></div>
<div class="feature-title script center" style="left:100px;top:988px">Free Shipping</div>
<div class="feature-title script center" style="left:460px;top:988px">Free Support</div>
<div class="feature-title script center" style="left:830px;top:988px">Price Guarantee</div>
<div class="feature-cap center" style="left:90px;top:1029px">GET A FREE DELIVERY ON ORDERS OF $200</div>
<div class="feature-cap center" style="left:450px;top:1029px">24/7 CUSTOMER SERVICE</div>
<div class="feature-cap center" style="left:824px;top:1029px">WE GUARANTEE THE BEST PRICE</div>

<!-- Feature products -->
<div class="abs script center" style="left:400px;top:1128px;width:400px;font-size:38px">Wonderful Flowers</div>
<h2 class="abs heading center" style="left:300px;top:1180px;width:600px;font-size:36px">Feature Products</h2>
<div class="ornament" style="top:1236px" role="img" aria-label="Leaf and flower divider ornament"></div>

<svg class="abs" style="left:33px;top:1482px" width="60" height="20" viewBox="0 0 60 20" fill="none" stroke="#e6b8c8" stroke-width="2"><line x1="2" y1="10" x2="58" y2="10"/><path d="M10 2L2 10l8 8"/></svg>
<svg class="abs" style="left:1100px;top:1482px" width="60" height="20" viewBox="0 0 60 20" fill="none" stroke="#1c1c1c" stroke-width="2"><line x1="2" y1="10" x2="58" y2="10"/><path d="M50 2l8 8-8 8"/></svg>

<div class="abs product-card"></div>
<div class="product-img" style="left:110px;background:radial-gradient(circle at 50% 30%,#d3132a 0%,#b50d22 30%,#f6d3de 60%,rgba(255,255,255,0) 72%)" role="img" aria-label="Bouquet of red carnations wrapped in pink paper"></div>
<div class="product-img" style="left:368px;background:radial-gradient(circle at 50% 35%,#8f2a6a 0%,#e8a0c6 35%,#f3c0d8 55%,rgba(255,242,236,0) 72%)" role="img" aria-label="Bouquet of purple and white blooms in pink wrap"></div>
<div class="product-img" style="left:632px;background:radial-gradient(circle at 50% 28%,#c81f4a 0%,#7a9a46 40%,rgba(255,255,255,0) 70%)" role="img" aria-label="Red tulips tied with twine"></div>
<div class="product-img" style="left:880px;background:radial-gradient(circle at 50% 28%,#f5f3ea 0%,#d8ddc8 30%,#7c9658 50%,rgba(255,255,255,0) 70%)" role="img" aria-label="White calla lily bouquet"></div>

<div class="product-name" style="left:75px">Name of product # 01</div>
<div class="product-price" style="left:75px">$40</div>
<div class="product-name" style="left:333px">Name of product # 01</div>
<div class="product-price" style="left:333px">$40</div>
<div class="product-name" style="left:597px">Name of product # 01</div>
<div class="product-price" style="left:597px">$40</div>
<div class="product-name" style="left:845px">Name of product # 01</div>
<div class="product-price" style="left:845px">$40</div>
<a class="btn" style="left:373px;top:1662px;width:135px;height:40px;font-size:12px;font-weight:400">Add To Cart
  <svg width="16" height="16" viewBox="0 0 16 16" fill="none" stroke="#1c1c1c" stroke-width="1.3"><path d="M2 5h12l-1 9H3z"/><path d="M5 5V3a3 3 0 0 1 6 0v2"/></svg>
</a>
<svg class="abs" style="left:418px;top:1688px" width="18" height="26" viewBox="0 0 18 26" fill="#fff" stroke="#1c1c1c" stroke-width="1.3"><path d="M2 2v18l5-4 4 8 3-1-4-8h6z"/></svg>

<!-- Welcome -->
<section class="abs welcome"></section>
<div class="abs" style="left:55px;top:1865px;width:610px;height:520px;background:radial-gradient(ellipse at 50% 35%,#e63f8f 0%,#b27ac8 25%,#f4ecdf 42%,#6f9a43 58%,rgba(249,217,232,0) 75%)" role="img" aria-label="Vase of pink roses, purple and white tulips"></div>
<div class="abs script" style="left:730px;top:1958px;font-size:40px">Welcome</div>
<h2 class="abs heading" style="left:730px;top:2010px;font-size:38px;line-height:46px">Exclusive Design by<br>Best Florists</h2>
<p class="abs" style="left:731px;top:2128px;width:370px;font-size:11px;line-height:18px;color:var(--muted)">Lorem Ipsum is simply dummy text of the printing and typesetting industry. Lorem Ipsum has been the industry's standard dummy text ever since the 1500s.</p>
<a class="btn" style="left:731px;top:2213px;width:170px;height:46px">SHOP NOW</a>

<!-- Blog -->
<div class="abs script center" style="left:400px;top:2452px;width:400px;font-size:38px">Articles</div>
<h2 class="abs heading center" style="left:300px;top:2505px;width:600px;font-size:36px">Blog Posts</h2>
<div class="ornament" style="top:2560px" role="img" aria-label="Leaf and flower divider ornament"></div>

<div class="blog-img" style="left:83px;background:linear-gradient(135deg,#f0d24a 0%,#eec3cf 25%,#f5eef0 55%,#c9b6d8 100%)" role="img" aria-label="Pink cherry blossom branches on white"></div>
<div class="blog-img" style="left:443px;background:linear-gradient(135deg,#4f6b30 0%,#f2a7ae 35%,#e9868f 65%,#3f5a28 100%)" role="img" aria-label="Pink carnations among green leaves"></div>
<div class="blog-img" style="left:803px;background:linear-gradient(135deg,#7a8f5c 0%,#eef0e6 40%,#f4f4ef 65%,#9fb37d 100%)" role="img" aria-label="White lilies in a vase by a window"></div>
<div class="blog-date" style="left:210px">june<span>2,2021</span></div>
<div class="blog-date" style="left:570px">june<span>2,2021</span></div>
<div class="blog-date" style="left:930px">june<span>2,2021</span></div>
<h3 class="blog-title heading" style="left:83px">Artcle title # 01</h3>
<h3 class="blog-title heading" style="left:443px">Artcle title # 02</h3>
<h3 class="blog-title heading" style="left:803px">Artcle title # 03</h3>
<p class="blog-text" style="left:83px">Lorem Ipsum is simply dummy text of the printing and typesetting industry. Lorem Ipsum has been the industry's standard dummy text ever since the 1500s.</p>
<p class="blog-text" style="left:443px">Lorem Ipsum is simply dummy text of the printing and typesetting industry. Lorem Ipsum has been the industry's standard dummy text ever since the 1500s.</p>
<p class="blog-text" style="left:803px">Lorem Ipsum is simply dummy text of the printing and typesetting industry. Lorem Ipsum has been the industry's standard dummy text ever since the 1500s.</p>
<a class="read-more" style="left:83px">Read More »</a>
<a class="read-more" style="left:443px">Read More »</a>
<a class="read-more" style="left:803px">Read More »</a>

<!-- Testimonials -->
<div class="abs script center" style="left:400px;top:3126px;width:400px;font-size:38px">Reviews</div>
<h2 class="abs heading center" style="left:300px;top:3176px;width:600px;font-size:36px">Testimonials</h2>
<div class="ornament" style="top:3234px" role="img" aria-label="Leaf and flower divider ornament"></div>
<div class="abs" style="left:286px;top:3323px;width:628px;height:262px;border-radius:34px;background:var(--cream)"></div>
<div class="abs" style="left:556px;top:3279px;width:88px;height:88px;border-radius:50%;background:radial-gradient(circle at 50% 40%,#e8b49c 0%,#b5654f 55%,#c96a6f 100%)" role="img" aria-label="Customer portrait"></div>
<p class="abs center" style="left:330px;top:3418px;width:540px;font-size:11px;line-height:18px"><span class="quote-mark">“</span> Lorem Ipsum is simply dummy text of the printing and typesetting industry. Lorem Ipsum has been the industry's standard dummy text ever since the 1500s, when an unknown printer took a galley of type and scrambled it to make a type specimen book. <span class="quote-mark">”</span></p>
<div class="abs script center" style="left:500px;top:3496px;width:200px;font-size:34px">Elena</div>
<span class="dot" style="left:582px;top:3547px"></span>
<span class="dot open" style="left:595px;top:3546px"></span>
<span class="dot" style="left:611px;top:3547px"></span>

<!-- Photo feed -->
<div class="abs script center" style="left:400px;top:3638px;width:400px;font-size:38px">Follow us on</div>
<h2 class="abs heading center" style="left:300px;top:3692px;width:600px;font-size:36px">Photofeed</h2>
<div class="ornament" style="top:3745px" role="img" aria-label="Leaf and flower divider ornament"></div>
<div class="insta-tile" style="left:78px;background:linear-gradient(135deg,#c7c0b8,#f3dcd3 50%,#e9cfc5)" role="img" aria-label="Blush peony bridal bouquet"></div>
<div class="insta-tile" style="left:288px;background:linear-gradient(135deg,#5c7a3c,#9ab6d8 45%,#eef2f4 70%,#6b8a49)" role="img" aria-label="Blue hydrangea and white rose bouquet"></div>
<div class="insta-tile" style="left:498px;background:linear-gradient(135deg,#2c3a25,#7a5cc0 40%,#a990de 70%,#3a3a3a)" role="img" aria-label="Purple flower bouquet"></div>
<div class="insta-tile" style="left:708px;background:linear-gradient(135deg,#f3e8ea,#f39aab 40%,#e77b90 70%,#f4f0f2)" role="img" aria-label="Pink roses in a vase"></div>
<div class="insta-tile" style="left:918px;background:linear-gradient(135deg,#3a2a3e,#9b4fa0 40%,#c988c9 70%,#5a3a6a)" role="img" aria-label="Purple bouquet held by a bride"></div>
<a class="btn" style="left:517px;top:4072px;width:170px;height:48px">FOLLOW US
  <svg width="16" height="16" viewBox="0 0 16 16" fill="none" stroke="#1c1c1c" stroke-width="1.5"><circle cx="8" cy="8" r="6.5"/></svg>
</a>

<!-- Footer -->
<section class="abs footer"></section>
<div class="abs newsletter"></div>
<div class="abs heading" style="left:138px;top:4264px;font-size:26px">Join us for our latest news updates</div>
<div class="abs" style="left:618px;top:4263px;width:305px;height:37px;border:2px solid var(--ink);border-radius:20px;padding:11px 16px;font-size:11px;font-style:italic">Email Address</div>
<a class="btn" style="left:929px;top:4263px;width:134px;height:37px;font-size:12px">SUBSCRIBE</a>

<div class="logo" style="left:74px;top:4495px;font-size:40px">Bloom &amp; Bough</div>

<h4 class="foot-h heading" style="left:467px">Quick links</h4>
<ul class="foot-list" style="left:467px;top:4500px">
  <li>Home</li><li>Shop</li><li>About</li><li>Blogs</li><li>Contact</li><li>Arrangement</li><li>bouquets</li><li>everlasting arrangements</li><li>gifts</li>
</ul>

<h4 class="foot-h heading" style="left:705px">Contact info.</h4>
<div class="contact-row" style="left:712px;top:4502px">
  <svg width="10" height="14" viewBox="0 0 10 14" fill="#1c1c1c"><path d="M5 0a5 5 0 0 1 5 5c0 4-5 9-5 9S0 9 0 5a5 5 0 0 1 5-5z"/><circle cx="5" cy="5" r="1.8" fill="#fff2ec"/></svg>
  <span>412 Willow Ln.<br>Fernvale, CA 90000</span>
</div>
<div class="contact-row" style="left:712px;top:4552px">
  <svg width="10" height="12" viewBox="0 0 10 12" fill="#1c1c1c"><path d="M2 0l3 3-1.5 2c1 2 2 3 3.5 4L9 8l1 3-2 1C4 12 0 7 0 2z"/></svg>
  <span>(+00) 555 010 220</span>
</div>
<div class="contact-row" style="left:712px;top:4578px">
  <svg width="10" height="10" viewBox="0 0 10 10" fill="none" stroke="#1c1c1c" stroke-width="1.4"><rect x="0.7" y="2" width="8.6" height="6"/><path d="M1 2l4 3 4-3"/></svg>
  <span>info@bloomandbough.com</span>
</div>

<h4 class="foot-h heading" style="left:980px">Social Links</h4>
<div class="social-row" style="left:987px;top:4502px"><i></i>Friendspace</div>
<div class="social-row" style="left:987px;top:4529px"><i></i>Chirpline</div>
<div class="social-row" style="left:987px;top:4556px"><i></i>Mailbox</div>
<div class="social-row" style="left:987px;top:4583px"><i></i>Photofeed</div>
<div class="social-row" style="left:987px;top:4610px"><i></i>Pinboard</div>

<div class="abs bottom-bar"></div>
<div class="abs" style="left:70px;top:4727px;font-size:12px">Copyright © 2021 Bloom &amp; Bough &nbsp;/&nbsp; Privacy Policy</div>
<div class="pay-chip" style="left:886px">Paylo</div>
<div class="pay-chip" style="left:934px">Kardo</div>
<div class="pay-chip" style="left:982px">Vexa</div>
<div class="pay-chip" style="left:1030px">Mestra</div>
<div class="pay-chip" style="left:1078px">Axon</div>

</body>
</html>
```